Belmora Wines

Hi all,

My name’s Liam Dowsett and I run a small wine brand based in the Canberra Wine District, Australia. I’m currently in the process of branding the business and am looking for a designer to help develop a new visual direction.

Background
I’ll be growing my own fruit from a leased vineyard site Named 'Wrenhollow' and my family’s property named 'Tibbard Vale', with a stronger emphasis on organic practices and site expression.

The Direction
The brand will centre around single vineyard wines, with each wine reflecting the unique site it comes from. I’d like the branding to support this idea of place, origin, and authenticity.

In terms of visual style, I’m drawn to something that is:

Simple and effective
A balance between traditional and modern
Clean, considered, and not overly decorative

Nothing too over-the-top, the goal is something timeless that lets the wine and vineyard story speak for itself.

At this stage, I’m mainly looking for:

Conceptual design direction / ideas
Label design (with potential to expand into broader branding)

I’m open to creative interpretation, so if the story resonates with you, I’d love to see how you would approach it.

Below I've attached an example of the bottle shape I will be using.

Cheers,
Liam

Colors
0054AA
0677BA
7BADD7
CADEEF
E8F1F8
FFC000
F8CF3A
FAE287
FDF2CF
FEFAEE

Requirements
Must have
• Mix of modern and traditional

```html
<!DOCTYPE html>
<html lang="en">
<head>
<meta charset="utf-8">
<title>Belmora Riesling Label</title>
<link rel="stylesheet" href="https://fonts.googleapis.com/css2?family=Marcellus&display=swap">
<style>
  :root {
    --backdrop: #d4d4d6;
    --paper: #fbfbf9;
    --ink: #16202e;
    --gold: #b8901c;
    --gold-light: #e3cc5a;
    --gold-deep: #8a6a12;
    --sky: #eeeeee;
  }
  * { margin: 0; padding: 0; box-sizing: border-box; }
  html, body {
    width: 1133px;
    height: 1200px;
    overflow: hidden;
    background: var(--backdrop);
  }
  .canvas {
    width: 1133px;
    height: 1200px;
    display: flex;
    align-items: center;
    justify-content: center;
  }
  .label {
    position: relative;
    width: 760px;
    height: 1140px;
    background: var(--paper);
    font-family: "Marcellus", serif;
    color: var(--ink);
    overflow: hidden;
  }
  .label__region {
    position: absolute;
    top: 78px;
    width: 100%;
    text-align: center;
    font-size: 30px;
    letter-spacing: 0.5px;
    white-space: nowrap;
  }
  .label__brand {
    position: absolute;
    top: 180px;
    left: 60px;
    right: 60px;
    text-align: center;
    font-size: 112px;
    font-weight: 400;
    line-height: 1;
    letter-spacing: 8px;
    font-kerning: none;
    white-space: nowrap;
    color: var(--gold);
  }
  .label__variety {
    position: absolute;
    top: 360px;
    width: 100%;
    text-align: center;
    font-size: 76px;
    font-weight: 400;
    letter-spacing: 2px;
    white-space: nowrap;
  }
  .label__landscape {
    position: absolute;
    top: 520px;
    left: 0;
    width: 100%;
    height: 530px;
    background:
      linear-gradient(180deg, var(--sky) 0%, var(--paper) 28%, var(--gold-light) 40%, #f3e8b8 60%, var(--gold-light) 100%);
  }
  .label__details {
    position: absolute;
    top: 1062px;
    width: 100%;
    text-align: center;
    font-size: 32px;
    word-spacing: 4px;
    white-space: nowrap;
  }
  .label__band {
    position: absolute;
    left: 0;
    bottom: 16px;
    width: 100%;
    height: 10px;
    background: linear-gradient(90deg, var(--gold-deep), var(--gold-light), var(--gold-deep));
  }
</style>
</head>
<body>
  <main class="canvas">
    <section class="label">
      <p class="label__region">Canberra Wine District, Australia</p>
      <h1 class="label__brand">BELMORA</h1>
      <h2 class="label__variety">RIESLING</h2>
      <div class="label__landscape" role="img" aria-label="Gold line engraving of rolling vineyard rows with a farmhouse, a line of cypress trees and soft clouds"></div>
      <p class="label__details">11.5% ALC/Vol | 750ml</p>
      <div class="label__band"></div>
    </section>
  </main>
</body>
</html>
```